Marlow Brochure

Brevik & Solan Education Group was formed in 2011 as an organizational arm
to put educational and charitable services together for community
development.

B & S was acquired by Marlow Education Group in 2013 and relocated to Texas
with the expressed focus of reaching underserved communities and
population, both in the Dallas- Fort Worth Metropolitan area and Houston
areas. Key members of the organization are based in Dallas, TX, Houston,
TX, Atlanta GA, and Washington DC and are strategically networked to
utilize their external resources for education advancement with
under-served populations.

Target Market(s)

- -The target market is 17-45 year olds, the demographics are 70%
women, 30% men, interested in an entry level education in
the health field

Industry/Entity Type

Education

```html
<!DOCTYPE html>
<html lang="en">
<head>
<meta charset="utf-8">
<title>Marlow Brochure – Application for Admission</title>
<link rel="stylesheet" href="https://fonts.googleapis.com/css2?family=Questrial&family=Tinos:ital,wght@1,700&display=swap">
<style>
  :root {
    --paper: #ffffff;
    --ink: #3a3a3a;
    --rule: #4a4a4a;
    --accent-green: #86bc25;
    --band-green: #93c01f;
    --panel-blue: #0f6194;
    --panel-text: #ffffff;
    --photo-light: #f7f3ef;
    --photo-warm: #e9dfd6;
  }
  * { box-sizing: border-box; margin: 0; padding: 0; }
  html, body { width: 1200px; height: 930px; overflow: hidden; background: var(--paper); }
  .brochure { position: relative; width: 1200px; height: 930px; background: var(--paper); font-family: "Questrial", sans-serif; color: var(--ink); }

  /* Application form panel */
  .application { position: absolute; left: 40px; top: 0; width: 546px; }
  .application__title { position: absolute; top: 66px; left: 0; width: 552px; text-align: center; font-family: "Tinos", serif; font-style: italic; font-weight: 700; font-size: 27px; color: var(--accent-green); }
  .form { position: absolute; top: 143px; left: 0; width: 546px; list-style: none; }
  .form__row { display: flex; align-items: flex-end; height: 20.7px; font-size: 13.4px; line-height: 1; white-space: nowrap; }
  .form__label { padding-bottom: 2px; }
  .form__line { flex: 1; border-bottom: 1px solid var(--rule); height: 1px; margin-bottom: 3px; }
  .form__line--short { flex: 0 0 auto; }
  .form__options { padding-bottom: 2px; word-spacing: 2px; }
  .gap { display: inline-block; width: 14px; }

  /* Right panel */
  .hero-photo { position: absolute; left: 600px; top: 0; width: 600px; height: 438px;
    background: linear-gradient(180deg, var(--photo-light) 0%, var(--photo-warm) 100%); }
  .info-panel { position: absolute; left: 600px; top: 438px; width: 600px; height: 468px; background: var(--panel-blue); color: var(--panel-text); }
  .info-panel__heading { position: absolute; left: 0; width: 590px; text-align: center; font-family: "Tinos", serif; font-style: italic; font-weight: 700; font-size: 24px; color: var(--accent-green); }
  .info-panel__text { position: absolute; left: 47px; width: 498px; font-size: 13.6px; line-height: 20.7px; }
  .mission-heading { top: 48px; }
  .mission-text { top: 100px; text-align: justify; }
  .history-heading { top: 188px; }
  .history-text { top: 236px; width: 492px; }
  .history-text p + p { margin-top: 20.7px; }
  .footer-band { position: absolute; left: 0; top: 906px; width: 1200px; height: 24px; background: var(--band-green); }
</style>
</head>
<body>
<main class="brochure">
  <section class="application">
    <h1 class="application__title">Application for Admission</h1>
    <ul class="form">
      <li class="form__row"><span class="form__label">Full Name:</span><span class="form__line"></span></li>
      <li class="form__row"><span class="form__label">Last</span><span class="form__line"></span></li>
      <li class="form__row"><span class="form__label">First</span><span class="form__line"></span></li>
      <li class="form__row"><span class="form__label">Middle</span><span class="form__line"></span></li>
      <li class="form__row"><span class="form__label">DOB:</span><span class="form__line"></span></li>
      <li class="form__row"><span class="form__label">Address:</span><span class="form__line"></span></li>
      <li class="form__row"><span class="form__label">Street Address</span><span class="form__line"></span></li>
      <li class="form__row"><span class="form__label">Apartment/Unit #</span><span class="form__line"></span></li>
      <li class="form__row"><span class="form__line"></span></li>
      <li class="form__row"><span class="form__label">City</span><span class="form__line form__line--short" style="width:125px"></span><span class="form__label">State</span><span class="form__line form__line--short" style="width:120px;margin-left:6px"></span><span class="form__label">ZIP Code</span><span class="form__line"></span></li>
      <li class="form__row"><span class="form__label">Phone:</span><span class="form__line"></span></li>
      <li class="form__row"><span class="form__label">Email</span><span class="form__line"></span></li>
      <li class="form__row"><span class="form__label">Social Security :</span><span class="form__line"></span></li>
      <li class="form__row"><span class="form__label">High School/ GED:</span><span class="form__line"></span></li>
      <li class="form__row"><span class="form__label">Graduation Year:</span><span class="form__line"></span></li>
      <li class="form__row"><span class="form__options">Semester:<span class="gap"></span>(Winter)<span class="gap"></span>(Spring)<span class="gap"></span>(Summer)<span class="gap"></span>(Fall)</span></li>
      <li class="form__row"><span class="form__options">Are you a citizen of the United States?<span class="gap"></span>YES 0R<span class="gap"></span>NO</span></li>
      <li class="form__row"><span class="form__options">If no, are you authorized to work in the U.S.?<span class="gap"></span>YES</span></li>
      <li class="form__row"><span class="form__options">0R<span class="gap"></span>NO</span></li>
      <li class="form__row"><span class="form__options">Have you ever been convicted of a felony?<span class="gap"></span>YES</span></li>
      <li class="form__row"><span class="form__options">0R<span class="gap"></span>NO</span></li>
      <li class="form__row"><span class="form__label">If yes, explain:</span><span class="form__line"></span></li>
      <li class="form__row"><span class="form__line"></span></li>
      <li class="form__row"><span class="form__line"></span></li>
      <li class="form__row"><span class="form__line"></span></li>
      <li class="form__row"><span class="form__label">Education</span><span class="form__line"></span></li>
      <li class="form__row"><span class="form__label">High School:</span><span class="form__line"></span></li>
      <li class="form__row"><span class="form__label">Address:</span><span class="form__line"></span></li>
      <li class="form__row"><span class="form__line"></span></li>
      <li class="form__row"><span class="form__line"></span></li>
      <li class="form__row"><span class="form__label">From:</span><span class="form__line form__line--short" style="width:125px"></span><span class="gap"></span><span class="form__label">To:</span><span class="form__line"></span></li>
      <li class="form__row"><span class="form__options">Did you graduate?<span class="gap"></span>YES 0R<span class="gap"></span>NO</span></li>
      <li class="form__row"><span class="form__options">0R</span></li>
      <li class="form__row"><span class="form__options">Diploma:</span></li>
    </ul>
  </section>

  <div class="hero-photo" role="img" aria-label="Photo of smiling students holding books and binders"></div>

  <section class="info-panel">
    <h2 class="info-panel__heading mission-heading">Our Mission</h2>
    <p class="info-panel__text mission-text">"Our primary mission is to develop high quality health professionals with the inspiration positively effect their families, communities and professions."</p>
    <h2 class="info-panel__heading history-heading">History</h2>
    <div class="info-panel__text history-text">
      <p>Brevik &amp; Solan Education Group was formed in 2011 as an organizational arm to put educational and charitable services together for community development.</p>
      <p>B &amp; S was acquired by Marlow Education Group in 2013 and relocated to Texas with the expressed focus of reaching underserved communities and population, both in the Dallas- Fort Worth Metropolitan area and Houston areas. Key members of the organization are based in Dallas, TX, Houston, TX and Washington DC and are strategically networked to utilize their external resources for education advancement with under-served populations.</p>
    </div>
  </section>

  <div class="footer-band"></div>
</main>
</body>
</html>
```